Banner Ad Design Project: Image banner for new website

Hi,

we need an image banner for a new website we just launched. The image banner should come in the formats 728x90 and 300x250.

The website the banner should advertise is http://www.vellora-tonebox.com/ .

We leave it up to your experience to find the best text and to obtain a great clickrate. Banner should be CATCHY and MOTIVATE people to enter. We do not want to include our current "logo". Will require all design files and fonts.

Best regards,
Brendan

```html
<!DOCTYPE html>
<html lang="en">
<head>
<meta charset="utf-8">
<title>Ambient Sounds Banners</title>
<link rel="stylesheet" href="https://fonts.googleapis.com/css2?family=Open+Sans:wght@400;600;700&display=swap">
<style>
  :root {
    --stage: #1e1e1e;
    --green-deep: #0a3d1c;
    --green-mid: #1f8a3a;
    --green-bright: #4fd15a;
    --teal-dark: #0b3b4a;
    --streak: #c9e86a;
    --text: #ffffff;
    --button-top: #d22a2a;
    --button-bottom: #6e0000;
    --button-edge: #4a0000;
  }
  * { margin: 0; padding: 0; box-sizing: border-box; }
  html, body {
    width: 1200px;
    height: 900px;
    overflow: hidden;
    background: var(--stage);
    font-family: "Open Sans", Arial, sans-serif;
    color: var(--text);
  }
  .canvas { position: relative; width: 1200px; height: 900px; }

  .banner { position: absolute; overflow: hidden; }
  .banner-art { position: absolute; inset: 0; }

  .banner--rectangle { left: 300px; top: 34px; width: 600px; height: 500px; }
  .banner--rectangle .banner-art {
    background:
      radial-gradient(ellipse 60% 40% at 85% 65%, rgba(201,232,106,0.45), transparent 70%),
      radial-gradient(ellipse 50% 60% at 20% 45%, rgba(79,209,90,0.55), transparent 70%),
      linear-gradient(160deg, var(--green-deep) 0%, var(--green-mid) 45%, var(--teal-dark) 75%, var(--green-mid) 100%);
  }

  .banner--leaderboard { left: 0; top: 646px; width: 1200px; height: 148px; }
  .banner--leaderboard .banner-art {
    background:
      radial-gradient(ellipse 30% 90% at 75% 40%, rgba(201,232,106,0.5), transparent 70%),
      radial-gradient(ellipse 40% 120% at 15% 50%, rgba(79,209,90,0.5), transparent 70%),
      linear-gradient(90deg, var(--green-mid) 0%, var(--green-deep) 35%, var(--green-mid) 60%, var(--teal-dark) 85%, var(--green-mid) 100%);
  }

  .headline {
    position: absolute;
    font-weight: 600;
    text-transform: uppercase;
    text-shadow: 0 2px 6px rgba(0,0,0,0.35);
  }
  .tagline {
    position: absolute;
    font-weight: 400;
    text-transform: uppercase;
    text-shadow: 0 2px 5px rgba(0,0,0,0.35);
  }

  .banner--rectangle .headline {
    left: 44px; top: 0;
    font-size: 78px;
    line-height: 70px;
    letter-spacing: 8px;
    padding-top: 66px;
  }
  .banner--rectangle .headline span { display: block; }
  .banner--rectangle .tagline {
    left: 46px; top: 290px;
    font-size: 38px;
    line-height: 52px;
    letter-spacing: 1px;
  }

  .banner--leaderboard .headline {
    left: 34px; top: 25px;
    font-size: 60px;
    line-height: 60px;
    letter-spacing: 10px;
    word-spacing: 22px;
  }
  .banner--leaderboard .tagline {
    left: 36px; top: 90px;
    font-size: 30px;
    line-height: 36px;
    letter-spacing: 1px;
  }

  .cta {
    position: absolute;
    display: flex;
    align-items: center;
    justify-content: center;
    gap: 18px;
    border: 2px solid var(--button-edge);
    border-radius: 16px;
    background: linear-gradient(180deg, var(--button-top) 0%, #a60d0d 50%, var(--button-bottom) 100%);
    box-shadow: inset 0 2px 0 rgba(255,255,255,0.35), 0 3px 8px rgba(0,0,0,0.4);
    color: var(--text);
    font-weight: 700;
    text-transform: uppercase;
    letter-spacing: 2px;
    text-decoration: none;
  }
  .cta svg { display: block; }
  .banner--rectangle .cta { left: 44px; top: 400px; width: 334px; height: 68px; font-size: 28px; }
  .banner--leaderboard .cta { left: 878px; top: 48px; width: 276px; height: 58px; font-size: 24px; border-radius: 12px; }
</style>
</head>
<body>
<main class="canvas">

  <section class="banner banner--rectangle" aria-label="300 by 250 banner">
    <div class="banner-art" role="img" aria-label="Abstract green light streaks and glowing sound waves"></div>
    <h1 class="headline"><span>Listen</span><span>Mix</span><span>Create</span></h1>
    <p class="tagline">A world of<br>ambient sounds</p>
    <a class="cta" href="#">Learn how
      <svg width="14" height="22" viewBox="0 0 14 22" aria-hidden="true"><path d="M3 3 L11 11 L3 19" fill="none" stroke="#fff" stroke-width="3.5"/></svg>
    </a>
  </section>

  <section class="banner banner--leaderboard" aria-label="728 by 90 banner">
    <div class="banner-art" role="img" aria-label="Abstract green light streaks and glowing sound waves"></div>
    <h2 class="headline">Listen Mix Create</h2>
    <p class="tagline">A world of ambient sounds</p>
    <a class="cta" href="#">Learn how
      <svg width="12" height="18" viewBox="0 0 12 18" aria-hidden="true"><path d="M2 2 L9 9 L2 16" fill="none" stroke="#fff" stroke-width="3"/></svg>
    </a>
  </section>

</main>
</body>
</html>
```